LUMEN Environmental needs an upgrade to its current business cards design

We need an upgrade to our current business cards design, where the LUMEN acronym is included, as possible and not being overloaded.
LUMEN Environmental is an Environmental Consultancy Firm based in Sydney.
We would like to see creative designs different from the standard type of business cards (for example, rounded edges, different to standard size of common business cards.

Target Market(s)

industrial companies (oil & gas, petrochemical, mining, insolvency, finance and manufacturing), developers, architect firms, law firms.

Industry/Entity Type

Business

Contact Information for Business Card

logos (brand and acronym), if they don't appear overloaded.
name
role
name of company (LUMEN Environmental),
address (Level 4, Suite 4B, 72-76 Wrenfield Street, Marlow Vale, NSW, 2093) landline (02 7314 2286)
mobile (staff member)
email (staff member) and
website (www.lumenverda.example).
Include: Contaminated Land, Site Remediation, Groundwater Assessment, Health and Ecological Risk Assessments, Acid Sulfate Soils, Waste Classification.

Font styles to use
Serif
Sans Serif

Requirements
Must have
• A creative design different to the standard type of business cards.
Nice to have
• Rounded edges
• Different size of business cards rather than the standard size.
Should not have
• Preferable not to use white colour background, unless it is required from a creative design proposed.
• Not an overloaded design.
• Avoid black colours

```html
<!DOCTYPE html>
<html lang="en">
<head>
<meta charset="utf-8">
<title>LUMEN Environmental – Business Card</title>
<link rel="stylesheet" href="https://fonts.googleapis.com/css2?family=Archivo+Black&family=Arimo:wght@400;700&display=swap">
<style>
  :root {
    --backdrop: #9a7c58;
    --lime-light: #c8ea3c;
    --lime: #9fd424;
    --lime-deep: #5f9e18;
    --tab-green: #a2d12a;
    --paper: #f4f4f4;
    --paper-shade: #dcdcdc;
    --ink: #2a2a2a;
    --white: #ffffff;
    --ghost: #d9ded0;
  }
  * { box-sizing: border-box; margin: 0; padding: 0; }
  html, body { width: 1200px; height: 1023px; overflow: hidden; }
  body {
    background: var(--backdrop);
    font-family: "Arimo", Arial, sans-serif;
    display: flex;
    flex-direction: column;
    align-items: center;
    justify-content: center;
    gap: 70px;
  }
  .card {
    position: relative;
    width: 600px;
    height: 360px;
    border-radius: 24px;
    overflow: hidden;
    box-shadow: 0 10px 24px rgba(0,0,0,.28);
  }

  /* Front */
  .card-front {
    background: radial-gradient(ellipse at 48% 42%, var(--lime-light) 0%, var(--lime) 45%, var(--lime-deep) 100%);
    color: var(--white);
  }
  .brand {
    position: absolute;
    left: 0; right: 0; top: 78px;
    text-align: center;
  }
  .brand-name {
    font-family: "Archivo Black", "Arimo", sans-serif;
    font-size: 104px;
    line-height: 1;
    letter-spacing: 2px;
  }
  .brand-sub {
    font-family: "Archivo Black", "Arimo", sans-serif;
    font-size: 25px;
    letter-spacing: 6px;
    margin-top: 4px;
    padding-left: 120px;
  }
  .services {
    position: absolute;
    left: 36px; right: 30px; bottom: 34px;
    font-size: 13px;
    line-height: 1.7;
    list-style: none;
    display: flex;
    flex-wrap: wrap;
    column-gap: 14px;
  }
  .services li::before {
    content: "";
    display: inline-block;
    width: 7px; height: 7px;
    border-radius: 50%;
    background: var(--white);
    margin-right: 6px;
    vertical-align: 1px;
  }

  /* Back */
  .card-back {
    background: linear-gradient(135deg, var(--white) 0%, var(--paper) 50%, var(--paper-shade) 100%);
    color: var(--ink);
  }
  .name-tab {
    position: absolute;
    left: 40px; top: 0;
    width: 230px; height: 170px;
    background: var(--tab-green);
    border-radius: 0 0 38px 38px;
    padding: 22px 20px 0 22px;
  }
  .person-name { font-size: 29px; color: var(--white); font-weight: 400; }
  .person-role { font-size: 15px; margin-top: 6px; color: var(--ink); }
  .contacts {
    position: absolute;
    left: 40px; top: 198px;
    list-style: none;
    font-size: 15px;
    line-height: 24px;
  }
  .contacts li { display: flex; align-items: flex-start; gap: 8px; }
  .contacts .icon { width: 14px; height: 14px; margin-top: 5px; flex: none; }
  .contacts .no-icon { padding-left: 22px; }
  .watermark-name {
    position: absolute;
    right: 18px; top: 24px;
    writing-mode: vertical-rl;
    font-family: "Archivo Black", "Arimo", sans-serif;
    font-size: 80px;
    line-height: 1;
    letter-spacing: 2px;
    color: var(--ghost);
  }
</style>
</head>
<body>

  <section class="card card-front" aria-label="Card front">
    <div class="brand">
      <div class="brand-name">LUMEN</div>
      <div class="brand-sub">ENVIRONMENTAL</div>
    </div>
    <ul class="services">
      <li>Contaminated Land</li>
      <li>Site Remediation</li>
      <li>Groundwater Assessment</li>
      <li>Waste Classification</li>
      <li>Health and Ecological Risk Assessments</li>
      <li>Acid Sulfate Soils</li>
    </ul>
  </section>

  <section class="card card-back" aria-label="Card back">
    <div class="name-tab">
      <h1 class="person-name">Miles Hartwell</h1>
      <p class="person-role">Project Engineer</p>
    </div>
    <ul class="contacts">
      <li class="no-icon">PO BOX 318</li>
      <li class="no-icon">Marlow Vale NSW 2093</li>
      <li>
        <svg class="icon" viewBox="0 0 14 14" aria-hidden="true"><circle cx="7" cy="7" r="6.2" fill="none" stroke="#8fc21f" stroke-width="1.2"/><path d="M4.6 3.6l1.4 1.6-.8 1c.6 1.2 1.4 2 2.6 2.6l1-.8 1.6 1.4-.8 1.2c-2.8-.4-5.2-2.8-5.6-5.6z" fill="#8fc21f"/></svg>
        0412 587 306
      </li>
      <li>
        <svg class="icon" viewBox="0 0 14 14" aria-hidden="true"><rect x="1" y="3" width="12" height="8.5" fill="none" stroke="#8fc21f" stroke-width="1.2"/><path d="M1 3l6 5 6-5" fill="none" stroke="#8fc21f" stroke-width="1.2"/></svg>
        miles@lumenverda.example
      </li>
      <li>
        <svg class="icon" viewBox="0 0 14 14" aria-hidden="true"><circle cx="7" cy="7" r="6" fill="none" stroke="#8fc21f" stroke-width="1.2"/><ellipse cx="7" cy="7" rx="2.6" ry="6" fill="none" stroke="#8fc21f" stroke-width="1"/><path d="M1 7h12" stroke="#8fc21f" stroke-width="1"/></svg>
        www.lumenverda.example
      </li>
    </ul>
    <div class="watermark-name" aria-hidden="true">LUMEN</div>
  </section>

</body>
</html>
```